Brochure Redesign

We need a new, adapted, design for our Brochure. A few weeks ago we've setup a new Homepage design and for now we want to adapt our old Brochure to the new design.

Requirements:
-) Place the 3 products quite prominent
-) Place also our add ons
-) Use the Keyvisuals you can find on the Homepage

New Homepage: www.rufkontor.at
Old Folder version - see attached

Requirements
Must have
• Logo and basic design from Homepage

```html
<!DOCTYPE html>
<html lang="de">
<head>
<meta charset="utf-8">
<title>Rufkontor – Produktfolder</title>
<link href="https://fonts.googleapis.com/css2?family=Dosis:wght@400;500;600;700&display=swap" rel="stylesheet">
<style>
:root{
  --bg:#e6e6e6;
  --paper:#ffffff;
  --paper-mid:#f1f1f1;
  --accent:#e9a92f;
  --accent-deep:#d38f1c;
  --red:#9b1f1f;
  --brown:#7b4a3e;
  --ink:#222;
  --muted:#8a8a8a;
  --rule:#e3b45a;
}
*{box-sizing:border-box;margin:0;padding:0}
html,body{width:1200px;height:1080px;overflow:hidden;background:var(--bg)}
body{font-family:'Dosis',sans-serif;color:var(--ink)}
.folder{position:absolute;left:60px;top:210px;width:1080px;height:660px;display:flex;box-shadow:0 20px 40px rgba(0,0,0,.18)}
.folder-bands{position:absolute;inset:0;z-index:0}
.panel{position:relative;width:360px;height:660px;padding:34px 14px 0 14px;z-index:1}
.panel--left{background:transparent}
.panel--mid{padding-top:66px}
.panel--right{padding:54px 18px 0 18px}
.pill{display:inline-block;border:2px solid var(--accent);border-radius:14px;padding:3px 10px;font-weight:700;font-size:13px;color:var(--brown);margin-bottom:12px}
.intro{font-size:10.5px;line-height:1.3;margin-bottom:10px}
.features{list-style:none}
.features li{position:relative;padding-left:14px;margin-bottom:7px;font-size:9.5px;line-height:1.2}
.features li::before{content:"✓";position:absolute;left:0;top:-1px;color:var(--red);font-weight:700;font-size:11px}
.features .name{display:block;color:var(--red);font-size:10.5px}
.section-title{font-weight:700;color:var(--brown);font-size:11.5px;margin:10px 0 6px}
.section-note{display:block;font-weight:400;color:var(--muted);font-size:9px}
.prices{display:flex;align-items:center;gap:18px;margin-top:8px}
.prices-label{font-weight:700;font-size:13px}
.price-table{border-collapse:collapse;font-size:10px}
.price-table td{padding:2px 4px;color:var(--red)}
.price-table td.amount{text-align:right;color:var(--ink);padding-left:24px}
.price-table tr.first td{border-bottom:1px solid var(--rule)}
.price-table .group{color:var(--ink);font-weight:700;font-size:9px}
.price-table .unit{color:var(--muted);font-size:9px}
.visual{position:absolute;border-radius:8px}
.visual--head{left:70px;top:460px;width:150px;height:170px;background:linear-gradient(160deg,#f5f5f5,#cfcfcf)}
.visual--mic{right:16px;top:54px;width:78px;height:128px;background:linear-gradient(180deg,#d9d9d9,#8c8c8c)}
.visual--cal{left:80px;top:480px;width:170px;height:130px;background:linear-gradient(160deg,#2f9a4a 0 18%,#e9e9e9 18%,#bdbdbd)}
.panel--mid .intro{width:180px;font-size:9.5px}
</style>
</head>
<body>
<main class="folder">
  <svg class="folder-bands" width="1080" height="660" viewBox="0 0 1080 660" aria-hidden="true">
    <rect x="0" y="0" width="360" height="660" fill="var(--paper)"/>
    <rect x="360" y="0" width="360" height="660" fill="var(--paper-mid)"/>
    <rect x="720" y="0" width="360" height="660" fill="var(--paper)"/>
    <path d="M0 440 H260 Q320 440 360 500 V660 H0Z" fill="var(--accent)"/>
    <path d="M360 555 Q540 600 720 560 V660 H360Z" fill="var(--accent-deep)"/>
    <path d="M720 640 Q900 610 1080 490 V660 H720Z" fill="var(--accent)"/>
  </svg>

  <section class="panel panel--left">
    <h2 class="pill">Online Wissensdatenbank</h2>
    <p class="intro">Unsere Online Wissensdatenbank stellt die Grundlage für die professionelle Sammlung Ihrer Informationen dar und dient als Schnittstelle zwischen Ihren Experten, CallCenter und Kunden. Strukturierte Informationsaufbereitung ermöglicht Suchanfragen nach Stichworten, Kategorien und/oder Freitext.</p>
    <ul class="features">
      <li><span class="name">Echtzeit Wissensmanagement</span>Alle Informationen werden online gewartet</li>
      <li><span class="name">Informationsaufbereitung</span>Fotos, Grafiken und Texte vermitteln Inhalte einfach und verständlich</li>
      <li><span class="name">Berechtigungen</span>Sie legen fest wer welche Informationen einsehen und verwalten darf</li>
      <li><span class="name">Suchfunktionen</span>Die integrierte Volltextsuche ermöglicht rasche Beantwortung von Fragen</li>
      <li><span class="name">Temporäre Informationen</span>Hinterlegen Sie zeitlich begrenzte Kampagnen oder Wartungsinformationen</li>
      <li><span class="name">Feedbackfunktion</span>Fragen oder Anmerkungen können per Mausklick übermittelt werden</li>
      <li><span class="name">Mitlernendes System</span>Laufende Kommunikation über die Wissensdatenbank führt zu kontinuierlicher Wissenserweiterung</li>
    </ul>
    <div class="prices">
      <span class="prices-label">Preise</span>
      <table class="price-table">
        <tr class="first"><td>Einmaliges Setup</td><td class="amount">99,00 €</td></tr>
        <tr><td>Monatliche Grundgebühr</td><td class="amount">19,00 €</td></tr>
      </table>
    </div>
    <div class="visual visual--head" role="img" aria-label="Illustration: Kopf im Profil mit bunten Zahnrädern"></div>
  </section>

  <section class="panel panel--mid">
    <h2 class="pill">Tonbänder &amp; Co</h2>
    <div class="visual visual--mic" role="img" aria-label="Illustration: silbernes Studiomikrofon"></div>
    <p class="intro">Sie haben die Möglichkeit mit neutralen und individuellen Bandansagen oder einer Anrufbeantworterfunktion Ihren Kunden noch mehr Service zu bieten.</p>
    <h3 class="section-title">Neutrale Bandansage</h3>
    <ul class="features">
      <li><span class="name">Neutrale Ansage</span>Ihr Kunde hört statt des Läutens ein neutrales Warteband (inkl. Musik)</li>
      <li><span class="name">Neutrales Offtime Band</span>Ihr Kunde hört außerhalb Ihrer Servicezeiten eine neutrale Ansage (inkl. Musik)</li>
    </ul>
    <h3 class="section-title">Personalisierte Bandansage<span class="section-note">(Produktion innerhalb von 7 Werktagen)</span></h3>
    <ul class="features">
      <li><span class="name">Individuelle Wartemusik</span>Ihr Kunde hört statt des Läutens ein personalisiertes Warteband nach Ihren Vorgaben (inkl. TKV freier Musik, max. 50 Wörter)</li>
      <li><span class="name">Individuelle Wartemusik</span>Ihr Kunde hört außerhalb Ihrer Servicezeiten eine personalisierte Ansage nach Ihren Vorgaben (inkl. TKV freier Musik, max. 100 Wörter)</li>
    </ul>
    <h3 class="section-title">Anrufbeantworterfunktion</h3>
    <ul class="features">
      <li><span class="name">Sprachbox</span>Ihr Kunde hört einen neutralen Sprachboxtext und kann eine Audio-Nachricht hinterlassen</li>
      <li><span class="name">Sofortige Weiterleitung</span>Sie erhalten direkt im Anschluss die Audio-Datei (Format mp3) per E-Mail zugesandt</li>
    </ul>
    <div class="prices">
      <span class="prices-label">Preise</span>
      <table class="price-table">
        <tr class="first"><td>Einmaliges Setup</td><td class="amount">0,00 €</td></tr>
        <tr><td class="group">Monatliche Gebühr</td><td></td></tr>
        <tr><td>Neutrale Bandansage</td><td class="amount">4,90 €</td></tr>
        <tr><td>Individuelle Bandansage</td><td class="amount">7,90 €</td></tr>
        <tr><td>Anrufbeantworterfunktion</td><td class="amount">9,90 €</td></tr>
      </table>
    </div>
  </section>

  <section class="panel panel--right">
    <h2 class="pill">Online Terminkalender</h2>
    <p class="intro">Sämtliche Anforderungen wie Terminlängen, Kategorien, Zeitfenster, etc. werden individuell an Ihre Bedürfnisse angepasst und ermöglichen ortsunabhängig alle Termine zu verwalten. Eine Tages- oder Wochenansicht bietet zusätzlich einen strukturierten Gesamtüberblick aller Termine.</p>
    <ul class="features">
      <li><span class="name">Online Kalender</span>Ortsunabhängige Online Terminverwaltung</li>
      <li><span class="name">Individuelle Terminkategorien und -längen</span>Sie legen fest welche Termine es gibt und wie lange diese dauern</li>
      <li><span class="name">Variable Terminfelder</span>Sie legen für jeden Termin die zu erfassenden Daten fest</li>
      <li><span class="name">Ansichten</span>Sie wählen zwischen Tages- und Wochenansicht</li>
      <li><span class="name">Terminverfügbarkeit</span>Sie legen fest wann welche Termine vergeben werden dürfen</li>
      <li><span class="name">Beliebige Kalenderanzahl</span>Terminvergabe für mehrere Standorte</li>
    </ul>
    <div class="prices" style="margin-top:40px">
      <span class="prices-label">Preise</span>
      <table class="price-table">
        <tr class="first"><td>Einmaliges Setup <span class="unit">(pro Kalender)</span></td><td class="amount">199,00 €</td></tr>
        <tr><td>Monatliche Grundgebühr <span class="unit">(pro Kalender)</span></td><td class="amount">29,00 €</td></tr>
      </table>
    </div>
    <div class="visual visual--cal" role="img" aria-label="Illustration: Wandkalender mit grüner Spiralbindung"></div>
  </section>
</main>
</body>
</html>
```